Website, SMS, Chat Linguabrook business

Im very open to the design, idea and card Shape. I just have my Web and business Names. Needs to be in Vector and PDF format Please. Based out of Miami, FL . Giving list of names to see what is the best naming and resonates with the brand. glossaverse-hub.com
linguabrook.com
pagewordshiftlabs.com everyvoicebridge.com. txt-polyglotia.com . rendertonguesco.com pagewordshiftlab.com.
talkmorphers.com

```html
<!DOCTYPE html>
<html lang="en">
<head>
<meta charset="UTF-8">
<title>Linguabrook Business Card</title>
<link href="https://fonts.googleapis.com/css2?family=Oswald:wght@400;500&family=Open+Sans:wght@400;600&display=swap" rel="stylesheet">
<style>
  :root {
    --stage: #cccccc;
    --ink: #141414;
    --panel-dark: #1e1e1e;
    --paper: #ffffff;
    --accent: #f05a28;
    --amber: #f7941d;
    --navy: #324598;
    --photo-light: #dfe2ea;
    --photo-dark: #3a3d48;
  }
  * { margin: 0; padding: 0; box-sizing: border-box; }
  html, body { width: 1049px; height: 1200px; overflow: hidden; }
  body { background: var(--stage); position: relative; font-family: "Oswald", sans-serif; }

  .card { position: absolute; left: 40px; width: 970px; height: 554px; overflow: hidden; }

  /* Front */
  .card-front { top: 28px; background: var(--ink); }
  .brand-mark {
    position: absolute; left: 445px; top: 150px; width: 80px; height: 80px;
    border: 6px solid var(--paper); border-radius: 50%;
  }
  .brand-name {
    position: absolute; left: 0; right: 0; top: 334px; text-align: center;
    color: var(--accent); font-family: "Oswald", sans-serif; font-weight: 400;
    font-size: 72px; line-height: 1;
  }
  .divider { position: absolute; left: 0; right: 0; top: 474px; height: 4px; background: var(--accent); }
  .web-pill {
    position: absolute; left: 317px; top: 439px; width: 363px; height: 72px;
    background: var(--accent); border-radius: 34px 0 34px 0;
    display: flex; align-items: center; justify-content: center; gap: 12px;
    color: var(--paper); font-family: "Open Sans", sans-serif; font-size: 20px;
  }
  .web-pill svg { width: 20px; height: 20px; }

  /* Back */
  .card-back { top: 615px; background: var(--paper); }
  .info-panel { position: absolute; left: 511px; top: 0; right: 0; bottom: 0; background: var(--panel-dark); }
  .accent-band { position: absolute; left: 0; top: 134px; width: 260px; height: 285px; background: var(--navy); }
  .halo { position: absolute; border-radius: 50%; }
  .halo-outer { left: 82px; top: 105px; width: 344px; height: 344px; background: var(--amber); }
  .halo-ring { position: absolute; left: 111px; top: 134px; width: 286px; height: 286px; border-radius: 50%; background: var(--accent); }
  .portrait {
    position: absolute; left: 124px; top: 147px; width: 260px; height: 260px; border-radius: 50%;
    background: linear-gradient(180deg, var(--photo-light) 0%, var(--photo-light) 45%, var(--photo-dark) 100%);
  }

  .contact-row { position: absolute; left: 493px; display: flex; align-items: center; }
  .contact-icon {
    width: 58px; height: 58px; border-radius: 50%; background: var(--paper);
    display: flex; align-items: center; justify-content: center;
    box-shadow: 0 2px 6px rgba(0,0,0,0.25);
  }
  .contact-icon svg { width: 24px; height: 24px; }
  .contact-text { position: absolute; left: 100px; white-space: nowrap; color: var(--paper); font-size: 28px; line-height: 1; }
  .person-name { font-size: 33px; font-weight: 400; }
  .person-role { display: block; font-size: 18px; margin-top: 10px; }

  .row-name { top: 88px; }
  .row-name .contact-text { top: 2px; }
  .row-phone { top: 191px; }
  .row-phone .contact-text { top: 12px; }
  .row-mail { top: 293px; }
  .row-mail .contact-text { top: 12px; }
  .row-web { top: 401px; }
  .row-web .contact-text { top: 12px; }
</style>
</head>
<body>
  <section class="card card-front">
    <div class="brand-mark"></div>
    <h1 class="brand-name">Linguabrook</h1>
    <div class="divider"></div>
    <div class="web-pill">
      <svg viewBox="0 0 24 24"><circle cx="12" cy="12" r="11" fill="#fff"/><path d="M6 7c2 0 3 2 5 2s1 3-1 4-1 4-3 4c-1-2-2-3-2-5s1-3 1-5zM15 5c2 1 4 3 4 6-2 0-3 1-3 3s-1 4-2 5c0-2-1-3-1-5s2-2 2-4-1-3 0-5z" fill="#f05a28"/></svg>
      <span>www.linguabrook.com</span>
    </div>
  </section>

  <section class="card card-back">
    <div class="accent-band"></div>
    <div class="halo halo-outer"></div>
    <div class="halo-ring"></div>
    <div class="portrait" role="img" aria-label="Portrait photo of the company's CEO"></div>
    <div class="info-panel"></div>

    <div class="contact-row row-name">
      <div class="contact-icon">
        <svg viewBox="0 0 24 24"><circle cx="12" cy="7.5" r="5" fill="#1e1e1e"/><path d="M3 22c0-5 4-8 9-8s9 3 9 8z" fill="#1e1e1e"/></svg>
      </div>
      <div class="contact-text"><span class="person-name">Dana Whitlock</span><span class="person-role">CEO</span></div>
    </div>

    <div class="contact-row row-phone">
      <div class="contact-icon">
        <svg viewBox="0 0 24 24"><path d="M6.6 2.5l3 3.5-2 2.5c1.3 3 3.6 5.3 6.5 6.6l2.5-2 3.5 3-1.8 3.4C12 19.5 4.5 12 3.2 4.3z" fill="#1e1e1e"/></svg>
      </div>
      <div class="contact-text">+1 305-555-0142</div>
    </div>

    <div class="contact-row row-mail">
      <div class="contact-icon">
        <svg viewBox="0 0 24 24"><rect x="2" y="5" width="20" height="14" rx="2" fill="none" stroke="#1e1e1e" stroke-width="2"/><path d="M3 6l9 7 9-7" fill="none" stroke="#1e1e1e" stroke-width="2"/></svg>
      </div>
      <div class="contact-text">info@linguabrook.com</div>
    </div>

    <div class="contact-row row-web">
      <div class="contact-icon">
        <svg viewBox="0 0 24 24"><circle cx="12" cy="12" r="10" fill="#1e1e1e"/><path d="M6 7c2 0 3 2 5 2s1 3-1 4-1 4-3 4c-1-2-2-3-2-5s1-3 1-5zM15 5c2 1 4 3 4 6-2 0-3 1-3 3s-1 4-2 5c0-2-1-3-1-5s2-2 2-4-1-3 0-5z" fill="#fff"/></svg>
      </div>
      <div class="contact-text">www.linguabrook.com</div>
    </div>
  </section>
</body>
</html>
```